Technology Podcast Cover Art Design

Title: The Wayfinders
Subtitle: A podcast about Conversations on tomorrow

site:

https://wayfindcast.example (ignore the colors/theme of site, we can change this as needed to suit new cover)

here is the description to give idea what podcast is about:
The Wayfinders is like a longform KIVO Lecture, a podcast about Conversations on tomorrow where look at the technologies, trends and societal norms shaping our collective future. Here the world’s disruptive top minds share their passion projects and how advances in genomics, robotics, space travel, IoT, artificial intelligence and other exponential tech is converging to create the future of tomorrow.

Two minds are better than one, and the purpose of this podcast is to create a worldwide “neural network” of connected human creators to tackle society’s big problems like climate change, aging, inequality, disease… you name it.

The #1 problem plaguing humanity is short term thinking. If in-depth, unscripted conversations with the scientists, startups and thought leaders daring to dream bigger is your cup of tea, you have come to the right place.

--

Target audience:
similar to Kivo.example, innovative creatives, scientists, startups, politicians... mainly smart people interested in future

Avoid:
DO NOT have a picture of a microphone in the cover art

What needs to be written:
the only thing that HAS to be written is: The Wayfinders

you can also add the subtitle (but you don't have to): A podcast about Conversations on tomorrow

you can also add host info (but you don't have to): with Lena Horvik

--

in terms of colors, we would prefer bright colors, probably blue or orange but if you make an awesome cover we can use that instead

```html
<!DOCTYPE html>
<html lang="en">
<head>
<meta charset="utf-8">
<title>The Wayfinders – Podcast Cover</title>
<link rel="stylesheet" href="https://fonts.googleapis.com/css2?family=Inter:wght@400;700&display=swap">
<style>
  :root {
    --sun-yellow: #ffeb00;
    --ink-black: #000000;
    --map-pink: #e9559a;
    --map-pink-light: #f3a9c8;
    --glow-cyan: #19b6e8;
  }
  html, body {
    margin: 0;
    padding: 0;
    width: 1200px;
    height: 1200px;
    overflow: hidden;
    background: var(--sun-yellow);
  }
  .cover {
    width: 1200px;
    height: 1200px;
    display: block;
    background: var(--sun-yellow);
  }
  .cover-title {
    font-family: "Inter", Helvetica, Arial, sans-serif;
    font-weight: 700;
    font-size: 134px;
    letter-spacing: -3px;
    fill: var(--ink-black);
  }
  .cover-subtitle {
    font-family: "Inter", Helvetica, Arial, sans-serif;
    font-weight: 400;
    font-size: 45px;
    fill: var(--ink-black);
  }
</style>
</head>
<body>
<svg class="cover" viewBox="0 0 1200 1200" xmlns="http://www.w3.org/2000/svg">
  <defs>
    <radialGradient id="world-fill" cx="50%" cy="50%" r="50%">
      <stop offset="0%" stop-color="var(--glow-cyan)" stop-opacity="0.55"/>
      <stop offset="45%" stop-color="var(--map-pink-light)"/>
      <stop offset="80%" stop-color="var(--map-pink)"/>
      <stop offset="100%" stop-color="var(--sun-yellow)" stop-opacity="0"/>
    </radialGradient>
  </defs>

  <rect class="backdrop" width="1200" height="1200" fill="var(--sun-yellow)"/>

  <circle class="world-illustration" role="img"
          aria-label="Illustration of a stylised globe with pink continents around a glowing centre"
          cx="630" cy="570" r="530" fill="url(#world-fill)"/>

  <text class="cover-title" x="14" y="637" textLength="1146" lengthAdjust="spacingAndGlyphs">The Wayfinders</text>

  <text class="cover-subtitle" x="614" y="714" text-anchor="middle">Conversations on tomorrow</text>
</svg>
</body>
</html>
```